Letterhead for clinic notes, test reports, and business cards

I need business card and letterheads for a medical clinic with the following:
1- Business cards. The back should allow for space for date and time of next appointments (few lines would do)
2- Letterhead for clinic notes
3- Letterhead for test reports.

Feel free to use whats included for examples. I value creativity so be creative.

Target Market(s)

Patients, referring physicians.

Industry/Entity Type

Health Care

Requirements
Must have
• Must use current logo.
• Must look good on white background
• Letterhead and reports must look good faxed.
• Please use themes of the current logo. Another possible color to use is grey as well (www.larchmontcardiac.org - use the font color in the text of that website)

```html
<!DOCTYPE html>
<html lang="en">
<head>
<meta charset="utf-8">
<title>Larchmont Cardiac Centre – Stationery</title>
<link href="https://fonts.googleapis.com/css2?family=Raleway:ital,wght@0,400;0,600;0,700;1,700&family=Open+Sans:ital,wght@0,400;0,700;1,400;1,700&display=swap" rel="stylesheet">
<style>
:root{
  --navy:#1d4a7d;
  --red:#e0222a;
  --red-dark:#b3161d;
  --grey:#5a5a5a;
  --paper:#ffffff;
  --backdrop:#e4e4e4;
  --rule:#c9c9c9;
}
*{box-sizing:border-box;margin:0;padding:0}
html,body{width:1200px;height:1200px;overflow:hidden;background:var(--backdrop);font-family:'Raleway',sans-serif;color:var(--grey)}
.canvas{position:relative;width:1200px;height:1200px}
.sheet{position:absolute;background:var(--paper);box-shadow:6px 6px 8px rgba(0,0,0,.35);border:1px solid #bdbdbd}
.abs{position:absolute}
.wordmark{position:absolute;text-align:center;font-family:'Raleway',sans-serif;font-weight:700;color:var(--navy);line-height:1.05;letter-spacing:.01em;white-space:nowrap}
.wordmark .dot{display:block;margin:0 auto;border-radius:50%;background:var(--red)}
.ecg{position:absolute;left:0;top:0;overflow:visible}
.ecg path{fill:none;stroke:var(--navy);stroke-width:1.4}
.ecg circle{fill:var(--navy)}

/* letterhead */
.letterhead{left:34px;top:53px;width:768px;height:1086px}
.letterhead .reg{left:699px;top:114px;font-size:11px}
.letterhead .contact-line{left:22px;top:150px;font-size:10.3px;white-space:nowrap}
.contact-line b{color:var(--navy);font-weight:700}

/* business card */
.card{left:865px;top:54px;width:291px;height:172px;overflow:hidden}
.card .holder{right:12px;top:12px;text-align:right;font-size:7.5px;line-height:1.4}
.card .holder strong{display:block;font-size:11.5px;color:#222;font-weight:700}
.card .org{right:12px;top:76px;text-align:right;font-size:6.8px;line-height:1.62}
.card .org strong{display:block;font-size:9.5px;color:#222;font-weight:700;line-height:1.3}
.band{position:absolute;left:0;right:0;bottom:0;height:20px;background:linear-gradient(90deg,var(--red),var(--red) 70%,var(--red-dark))}
.band span{position:absolute;left:10px;top:5px;font-size:7.2px;color:#fff}

/* appointment card */
.appt{left:865px;top:250px;width:291px;height:171px;overflow:hidden}
.appt .title{left:8px;top:39px;font-size:8.5px;font-weight:600;color:#444}
.appt .write-line{position:absolute;left:8px;right:12px;height:1px;background:var(--rule)}

/* report */
.report{left:633px;top:439px;width:526px;height:682px;font-family:'Open Sans',sans-serif;color:#111}
.report .org{right:22px;top:37px;text-align:right;font-size:6.4px;line-height:1.5;color:var(--grey);font-family:'Raleway',sans-serif}
.report .org strong{display:block;font-size:9.3px;color:var(--navy);font-weight:700}
.field{position:absolute;font-size:6.4px;font-weight:700;white-space:nowrap}
.field.colon::after{content:":";position:absolute;left:53px}
.hr{position:absolute;left:44px;width:455px;background:#111}
.study-title{left:0;right:0;top:236px;text-align:center;font-size:11px;font-weight:700;font-style:italic}
.vessels{position:absolute;left:106px;top:269px;width:330px;border:1.2px solid #333;border-collapse:collapse;font-size:5.4px;table-layout:fixed}
.vessels th{font-weight:400;border:0.6px solid #777;height:9px;padding:0}
.vessels td{height:9.4px;padding:0 2px;border-left:0.6px solid #999;border-right:0.6px solid #999}
.vessels td.name{text-align:right}
.vessels .box{display:block;width:7px;height:7px;border:0.6px solid #999;margin-left:2px}
.note-label{position:absolute;left:44px;font-size:6.6px;font-weight:700;font-style:italic;color:var(--red)}
.note-label::after{content:":";position:absolute;left:54px}
.sig{position:absolute;font-size:6.4px;font-weight:700;font-style:italic;white-space:nowrap}
</style>
</head>
<body>
<div class="canvas">

  <!-- Letterhead: clinic notes -->
  <section class="sheet letterhead" aria-label="Clinic notes letterhead">
    <div class="wordmark" style="left:22px;top:20px;width:224px;font-size:19px">
      <span class="dot" style="width:34px;height:34px;margin-bottom:30px"></span>LARCHMONT CARDIAC<br><span style="font-size:16px">CENTRE</span>
    </div>
    <svg class="ecg" width="768" height="200">
      <path d="M24 139 H646 L653 143 L658 153 L661 97 L665 155 L670 140 L675 136 L683 139 H755"/>
      <circle cx="24" cy="139" r="2.6"/><circle cx="755" cy="139" r="2.6"/>
    </svg>
    <div class="abs reg">Reg: 1234</div>
    <div class="abs contact-line">1187 Ferncliff Road, Suite 310, Kingsbridge ON K4R2T8 <b>|</b> phone 555-214-7730 <b>|</b> fax 555-214-7731 <b>|</b> email hello@larchmontcardiac.org</div>
  </section>

  <!-- Business card front -->
  <section class="sheet card" aria-label="Business card">
    <div class="wordmark" style="left:8px;top:10px;width:150px;font-size:12.5px">
      <span class="dot" style="width:24px;height:24px;margin-bottom:22px"></span>LARCHMONT CARDIAC<br><span style="font-size:10px">CENTRE</span>
    </div>
    <div class="abs holder"><strong>Card Holders Name</strong>ABC, DEFG, Abc (DEF)<br>Position</div>
    <div class="abs org"><strong>Larchmont Cardiac Centre</strong>1187 Ferncliff Road,<br>Suite 310, Kingsbridge ON K4R2T8<br>Phone 555-214-7730<br>Fax 555-214-7731<br>Email : hello@larchmontcardiac.org</div>
    <svg class="ecg" width="291" height="172">
      <path d="M4 147 H124 L129 150 L133 157 L135 116 L138 160 L142 149 L146 145 L152 147 H286"/>
      <circle cx="4" cy="147" r="2"/><circle cx="286" cy="147" r="2"/>
    </svg>
    <div class="band"><span>www.larchmontcardiac.org</span></div>
  </section>

  <!-- Business card back: appointment -->
  <section class="sheet appt" aria-label="Appointment card">
    <div class="wordmark" style="left:200px;top:10px;width:80px;font-size:6.8px">
      <span class="dot" style="width:14px;height:14px;margin-bottom:6px"></span>LARCHMONT CARDIAC<br><span style="font-size:5.6px">CENTRE</span>
    </div>
    <div class="abs title">Next appointment</div>
    <div class="write-line" style="top:58px"></div>
    <div class="write-line" style="top:70px"></div>
    <div class="write-line" style="top:82px"></div>
    <div class="write-line" style="top:94px"></div>
    <div class="write-line" style="top:106px"></div>
    <div class="write-line" style="top:118px"></div>
    <div class="write-line" style="top:130px"></div>
    <svg class="ecg" width="291" height="171">
      <path d="M4 154 H259 L263 157 L266 162 L268 135 L271 164 L275 155 L278 152 L283 154 H287"/>
      <circle cx="4" cy="154" r="1.8"/>
    </svg>
    <div class="band"><span>www.larchmontcardiac.org</span></div>
  </section>

  <!-- Test report -->
  <section class="sheet report" aria-label="Test report letterhead">
    <div class="wordmark" style="left:24px;top:22px;width:150px;font-size:12.5px">
      <span class="dot" style="width:30px;height:30px;margin-bottom:14px"></span>LARCHMONT CARDIAC<br><span style="font-size:10px">CENTRE</span>
    </div>
    <div class="abs org"><strong>Larchmont Cardiac Centre</strong>1187 Ferncliff Road,<br>Suite 310, Kingsbridge ON K4R2T8<br>phone 555-214-7730<br>fax 555-214-7731<br>email hello@larchmontcardiac.org</div>
    <svg class="ecg" width="526" height="140">
      <path d="M25 102 H360 L366 105 L371 111 L374 74 L378 114 L382 104 L387 100 L394 102 H502"/>
      <circle cx="25" cy="102" r="2"/><circle cx="502" cy="102" r="2"/>
    </svg>

    <div class="field colon" style="left:44px;top:124px">Name</div>
    <div class="field colon" style="left:44px;top:137px">Exam ID</div>
    <div class="field colon" style="left:44px;top:150px">Exam Dat</div>
    <div class="field colon" style="left:44px;top:176px">Risk Factors</div>
    <div class="field colon" style="left:44px;top:215px">Medication</div>
    <div class="field" style="left:239px;top:124px">Med Rec No.</div>
    <div class="field" style="left:239px;top:137px">Date Of Birth:</div>
    <div class="field" style="left:314px;top:137px">Age</div>
    <div class="field" style="left:359px;top:137px">Sex</div>
    <div class="field" style="left:239px;top:150px">Referred By</div>
    <div class="field" style="left:239px;top:163px">V.S. History</div>
    <div class="field" style="left:239px;top:215px">Reason for Study</div>
    <div class="field" style="left:456px;top:150px">Admition</div>
    <div class="field" style="left:456px;top:163px">Room#</div>
    <div class="field" style="left:456px;top:176px">Prior Exam</div>
    <div class="field" style="left:456px;top:189px">Limited</div>

    <div class="hr" style="top:232px;height:1.6px"></div>
    <div class="abs study-title">Aneurysm Surway</div>
    <div class="hr" style="top:255px;height:.7px;background:#555"></div>

    <table class="vessels">
      <colgroup><col style="width:52px"><col><col><col><col><col><col></colgroup>
      <thead>
        <tr><th rowspan="2">Vessel</th><th colspan="3">Right</th><th colspan="3">Left</th></tr>
        <tr><th>A-P</th><th>Lat</th><th>Thrombus</th><th>A-P</th><th>Lat</th><th>Thrombus</th></tr>
      </thead>
      <tbody>
        <tr><td class="name">Prox CFA</td><td></td><td></td><td><span class="box"></span></td><td></td><td></td><td><span class="box"></span></td></tr>
        <tr><td class="name">Mid CFA</td><td></td><td></td><td><span class="box"></span></td><td></td><td></td><td><span class="box"></span></td></tr>
        <tr><td class="name">Distal CFA</td><td></td><td></td><td><span class="box"></span></td><td></td><td></td><td><span class="box"></span></td></tr>
        <tr><td class="name">Prox SFA</td><td></td><td></td><td><span class="box"></span></td><td></td><td></td><td><span class="box"></span></td></tr>
        <tr><td class="name">Mid SFA</td><td></td><td></td><td><span class="box"></span></td><td></td><td></td><td><span class="box"></span></td></tr>
        <tr><td class="name">Distal SFA</td><td></td><td></td><td><span class="box"></span></td><td></td><td></td><td><span class="box"></span></td></tr>
        <tr><td class="name">Prox POP</td><td></td><td></td><td><span class="box"></span></td><td></td><td></td><td><span class="box"></span></td></tr>
        <tr><td class="name">Mid Pop</td><td></td><td></td><td><span class="box"></span></td><td></td><td></td><td><span class="box"></span></td></tr>
        <tr><td class="name">Distal Pop</td><td></td><td></td><td><span class="box"></span></td><td></td><td></td><td><span class="box"></span></td></tr>
      </tbody>
    </table>

    <div class="hr" style="top:389px;height:.7px;background:#555"></div>

    <div class="note-label" style="top:429px">Interpretation</div>
    <div class="note-label" style="top:468px">Impression</div>

    <div class="abs" style="left:41px;top:527px;width:224px;height:.7px;background:#777"></div>
    <div class="sig" style="left:41px;top:535px">Name &amp; Signature</div>
    <div class="sig" style="left:208px;top:535px">Date:</div>
    <div class="sig" style="left:282px;top:522px;font-weight:400">performed By <span style="margin-left:10px">:</span></div>
    <div class="sig" style="left:282px;top:535px;font-weight:400">Transcribed <span style="margin-left:14px">:</span></div>
    <div class="sig" style="right:22px;top:560px;font-weight:400">Report Prepared by CardioLedger Records System</div>
  </section>

</div>
</body>
</html>
```